CD Cover Design with skull

We need a simple CD cover, front square only for an upcoming single. The cover should be black or some texturized black(ish) color with the skull image attached (or an original likeness) featured prominently, either centrally, or perhaps oversized and emerging onto the cover from the left side, with maybe half of the actual skull being visible. The cover must read "Calvin Marsh" and "Left by Dawn" preferrrably in a simple white font. Thank you!
Target Market(s)
Rock and roll / country music fans
Industry/Entity Type
Music Download
Look and feel
Each slider illustrates characteristics of the customer's brand and the style your logo design should communicate.

```html
<!DOCTYPE html>
<html lang="en">
<head>
<meta charset="utf-8">
<title>Calvin Marsh – Left by Dawn</title>
<link rel="stylesheet" href="https://fonts.googleapis.com/css2?family=Germania+One&display=swap">
<style>
  :root {
    --night: #0c0c0c;
    --beam: #000000;
    --bone-light: #efe6cf;
    --bone-mid: #cdbb92;
    --bone-shadow: #6e5a3a;
    --ink-light: #e8dfe2;
  }
  html, body {
    margin: 0;
    padding: 0;
    width: 1200px;
    height: 1200px;
    overflow: hidden;
    background: var(--night);
  }
  .cover {
    position: relative;
    width: 1200px;
    height: 1200px;
    background: var(--night);
  }
  .cover__art {
    position: absolute;
    inset: 0;
    width: 1200px;
    height: 1200px;
    display: block;
  }
  .film-perforation { fill: var(--ink-light); }
  .light-beam { fill: var(--beam); }
  .cover-title {
    font-family: "Germania One", "Times New Roman", serif;
    fill: var(--ink-light);
    font-size: 150px;
  }
</style>
</head>
<body>
<main class="cover">
  <svg class="cover__art" viewBox="0 0 1200 1200" xmlns="http://www.w3.org/2000/svg">
    <defs>
      <radialGradient id="bone-tone" cx="45%" cy="35%" r="70%">
        <stop offset="0%" stop-color="var(--bone-light)"/>
        <stop offset="60%" stop-color="var(--bone-mid)"/>
        <stop offset="100%" stop-color="var(--bone-shadow)"/>
      </radialGradient>
      <pattern id="perforations" x="24" y="0" width="77.3" height="62" patternUnits="userSpaceOnUse">
        <rect class="film-perforation" x="0" y="0" width="40" height="62"/>
      </pattern>
    </defs>

    <polygon class="light-beam" points="0,156 1200,376 1200,760 0,1072"/>

    <rect class="film-strip film-strip--top" x="0" y="0" width="1200" height="62" fill="url(#perforations)"/>
    <rect class="film-strip film-strip--bottom" x="0" y="1138" width="1200" height="62" fill="url(#perforations)" transform="translate(0 0)"/>

    <ellipse class="skull-artwork" cx="592" cy="600" rx="132" ry="220"
             fill="url(#bone-tone)" role="img"
             aria-label="Illustration of a weathered human skull with a trickle of blood at the mouth"/>

    <g class="artist-name">
      <text class="cover-title" x="28" y="604" textLength="404" lengthAdjust="spacingAndGlyphs">Calvin</text>
      <text class="cover-title" x="28" y="724" textLength="404" lengthAdjust="spacingAndGlyphs">Marsh</text>
    </g>
    <g class="single-title">
      <text class="cover-title" x="744" y="604" textLength="432" lengthAdjust="spacingAndGlyphs">Left by</text>
      <text class="cover-title" x="744" y="724" textLength="236" lengthAdjust="spacingAndGlyphs">DAWN</text>
    </g>
  </svg>
</main>
</body>
</html>
```